Gummy Label design for hemp company

I need a 3.25 inch wide by 4 inch tall label made to be put on bags of gummies. I will include all disclaimers that need to be there, as well as my logo. This is for our 25 mg Delta 8 gummies 20ct, but I will use the design for our entire gummy line, just editing the text. Needs to have ingredient list. Ingredients: Sugar, Inulin, Corn syrup, water, pectin, citric acid, baking soda, fruit, hemp extract.

Everything should be on one label as this is going on a sticker that will be placed on a bag.
I would like to highlight that they are vegan if possible.

• Must have the following disclaimer: "Contains Farm Bill compliant hemp extract. These statements have not been evaluated by the KWT. This product is NOT intended to treat, cure, or prevent any disease. Do not operate heavy machinery while using this product. This product may cause you to fail a drug test. Consult with your doctor before trying any new products. Do not take if pregnant or lactating. If you experience any adverse effects, discontinue use and seek advice from your physician."
• NEEDS TO SAY: "100% hemp derived" also "<.3% D9 THC"

```html
<!DOCTYPE html>
<html lang="en">
<head>
<meta charset="utf-8">
<title>SunnyDay Hemp – Delta 8 Gummies Label</title>
<link href="https://fonts.googleapis.com/css2?family=Graduate&family=Ubuntu:wght@400;500;700&display=swap" rel="stylesheet">
<style>
  :root{
    --green:#2f8a17;
    --lime:#8fe000;
    --white:#ffffff;
    --backdrop:#e6e6e6;
    --candy-red:#e0213a;
    --candy-orange:#f57a1e;
    --candy-yellow:#f7d628;
  }
  *{margin:0;padding:0;box-sizing:border-box}
  html,body{width:1009px;height:1200px;overflow:hidden;background:var(--backdrop)}
  body{position:relative;font-family:"Ubuntu",sans-serif;color:var(--green)}
  .label{position:absolute;left:154px;top:169px;width:700px;height:862px;background:var(--white)}
  .abs{position:absolute}
  .badge-hemp{left:28px;top:25px;width:118px;height:118px;border:2px solid var(--green);border-radius:50%;
    display:flex;flex-direction:column;align-items:center;justify-content:center;line-height:.95;font-weight:400}
  .badge-hemp .big{font-size:31px}
  .badge-hemp .small{font-size:19px;margin-top:2px}
  .badge-thc{left:571px;top:25px;width:100px;height:100px;border-radius:50%;background:var(--green);color:var(--white);
    display:flex;flex-direction:column;align-items:center;justify-content:center;line-height:1}
  .badge-thc .big{font-size:31px}
  .badge-thc .small{font-size:22px;font-weight:500;margin-top:3px}
  .brand{left:0;top:60px;width:700px;display:flex;flex-direction:column;align-items:center}
  .brand-dot{width:54px;height:54px;border-radius:50%;background:var(--lime)}
  .brand-name{margin-top:14px;font-size:38px;font-weight:700;color:var(--green);letter-spacing:-.5px}
  .title{left:0;top:243px;width:700px;text-align:center;font-family:"Graduate",sans-serif;font-size:60px;
    color:var(--green);letter-spacing:1px;line-height:1}
  .dose{left:182px;top:318px;width:336px;height:47px;border-radius:24px;background:var(--lime);color:var(--white);
    font-size:31px;font-weight:700;letter-spacing:-1px;display:flex;align-items:center;justify-content:center}
  .product-photo{left:178px;top:374px;width:349px;height:189px;border-radius:40px;
    background:radial-gradient(ellipse at 25% 40%,var(--candy-red) 0%,transparent 45%),
               radial-gradient(ellipse at 55% 55%,var(--candy-orange) 0%,transparent 50%),
               radial-gradient(ellipse at 85% 45%,var(--candy-yellow) 0%,transparent 45%),
               linear-gradient(90deg,#fbe9a0,#fbc9a0,#fbe9a0)}
  .ingredients{left:35px;top:589px;width:445px;height:86px;border:2px solid var(--green);border-radius:9px;
    display:flex;align-items:center;justify-content:center;text-align:center;padding:10px 8px 0;
    font-size:19.5px;font-weight:700;line-height:1.5;letter-spacing:-.3px}
  .ingredients-tab{left:161px;top:572px;width:192px;height:33px;border-radius:17px;background:var(--green);color:var(--white);
    font-size:20px;font-weight:500;display:flex;align-items:center;justify-content:center}
  .claim{top:585px;width:80px;display:flex;flex-direction:column;align-items:center}
  .claim svg{width:68px;height:68px}
  .claim span{margin-top:8px;font-size:13px;font-weight:500}
  .claim-vegan{left:492px}
  .claim-usa{left:578px}
  .disclaimer{left:29px;top:684px;width:643px;height:151px;border:2px solid var(--green);border-radius:12px;
    padding:11px 17px;font-size:16px;line-height:21.5px;text-align:justify}
</style>
</head>
<body>
<main class="label">
  <div class="abs badge-hemp"><span class="big">100%</span><span class="big">HEMP</span><span class="small">DERIVED</span></div>
  <div class="abs badge-thc"><span class="big">&lt;.3%</span><span class="small">D9 THC</span></div>

  <div class="abs brand"><div class="brand-dot"></div><div class="brand-name">SunnyDay Hemp</div></div>

  <h1 class="abs title">DELTA 8 GUMMIES</h1>
  <div class="abs dose">25MG PER GUMMY</div>

  <div class="abs product-photo" role="img" aria-label="Pile of red, orange, yellow and purple gummy bears"></div>

  <div class="abs ingredients">Sugar, Inulin, Corn syrup, water, pectin, citric acid, baking soda, fruit, hemp extract.</div>
  <div class="abs ingredients-tab">INGREDIENTS</div>

  <div class="abs claim claim-vegan">
    <svg viewBox="0 0 68 68" aria-hidden="true">
      <circle cx="34" cy="34" r="32" fill="none" stroke="var(--lime)" stroke-width="2"/>
      <path d="M33 49 C18 49 14 36 16 25 C26 24 34 30 33 49Z" fill="var(--green)"/>
      <path d="M35 47 C36 32 42 24 53 22 C55 36 48 46 35 47Z" fill="var(--green)"/>
    </svg>
    <span>VEGAN</span>
  </div>
  <div class="abs claim claim-usa">
    <svg viewBox="0 0 68 68" aria-hidden="true">
      <circle cx="34" cy="34" r="32" fill="none" stroke="var(--lime)" stroke-width="2"/>
      <clipPath id="flag-clip"><circle cx="34" cy="34" r="27"/></clipPath>
      <g clip-path="url(#flag-clip)" fill="var(--green)">
        <rect x="0" y="8" width="68" height="4"/><rect x="0" y="16" width="68" height="4"/>
        <rect x="0" y="24" width="68" height="4"/><rect x="0" y="32" width="68" height="4"/>
        <rect x="0" y="40" width="68" height="4"/><rect x="0" y="48" width="68" height="4"/>
        <rect x="0" y="56" width="68" height="4"/><rect x="0" y="0" width="32" height="32"/>
      </g>
    </svg>
    <span>USA ORIGIN</span>
  </div>

  <p class="abs disclaimer">Contains Farm Bill compliant hemp extract. These statements have not been evaluated by the KWT. This product is NOT intended to treat, cure, or prevent any disease. Do not operate heavy machinery while using this product. This product may cause you to fail a drug test. Consult with your doctor before trying any new products. Do not take if pregnant or lactating. If you experience any adverse effects, discontinue use and seek advice from your physician.</p>
</main>
</body>
</html>
```